Pet Shop Website

website will need to have the following features:
• Photo Galleries of each species (Dogs, Cats, Birds, Fish, Reptiles, Rabbits) in a light box popup
o Each species may have several different categories for example:
 Fish
• Marine fish
• Fresh water
• tropical
• Cichlid
• Information Fact sheets of each species – Downloaded as a pdf which can be either
o Care Sheets
o Training Sheets
• Members Area
o Username (Email Address) & Password login
o New signups
o Exclusive Member Deals
o Newsletter options

The front page must be very simple (for example lumavest.com.au) contain the following:
• Product of the week - which can be purchased online
o Short details
o Cost
• Pet Club Sign up picture
• Animal of the week/month
• Contact Phone Number and addresses of the stores
• A jQuery slideshow (Images could include stores, pets etc…)
The main page MUST keep simple. We do not want it cluttered.

Inner Page
The animals / reptile page will need to have:
• Short description of the species
• Photo Galleries
• A list of what is in stock and the list needs to clearly be sorted by each store (Use of Tabs maybe).
• Facts sheets / Info sheets
The type of website ideas (not the type of look that we are necessary after) is and the sort of content that we want to offer are as follows:

http://www.scalenook.com.au/
http://www.brindlecovepaws.com.au/
http://www.thefurrowden.com.au
http://www.tailtown.net.au

Colour in the new website:
Blue
Red
Grey
Yellow

Original site:

http://www.critterglow.com.au
Updates

Hi Guys,

We had feedback from the client and they would like to see a few dark designs.

Thanks                                   

Reason: We would like to reopen this contest back up for a further week

Target Market(s)

Targeting animal lovers

Industry/Entity Type

Store

Requirements
Should not have
• Alter the logo in anyway

```html
<!DOCTYPE html>
<html lang="en">
<head>
<meta charset="utf-8">
<title>Critter Glow – Pet Superstores</title>
<link rel="stylesheet" href="https://fonts.googleapis.com/css2?family=Arimo:wght@400;700&family=Libre+Baskerville:wght@400;700&family=Alfa+Slab+One&display=swap">
<style>
:root{
  --page:#cbcbcb;
  --wine:#6e0508;
  --wine-dark:#570305;
  --navy:#131c55;
  --panel:#efefef;
  --panel-border:#ffffff;
  --ink:#111111;
  --price:#7a0a0a;
  --gold:#f0b400;
  --gold-dark:#d99300;
  --yellow:#ffe21a;
  --rule:#9a9a9a;
  --teal:#6fa89a;
}
*{box-sizing:border-box;margin:0;padding:0}
html,body{width:1200px;height:1084px;overflow:hidden}
body{background:var(--page);font-family:Arimo,Arial,sans-serif;color:var(--ink);position:relative}
.abs{position:absolute}
.top-strip{left:0;top:0;width:1200px;height:6px;background:var(--wine)}

.brand{left:150px;top:60px;width:260px;font-family:"Libre Baskerville",Georgia,serif;font-weight:700;font-size:36px;color:var(--wine);text-align:center;line-height:1}

.main-nav{left:560px;top:56px;width:496px;height:54px}
.main-nav svg{position:absolute;left:0;top:0}
.main-nav ul{list-style:none;position:absolute;left:0;top:0;width:100%;height:100%}
.main-nav li{position:absolute;top:18px;font-family:"Libre Baskerville",Georgia,serif;font-weight:700;font-size:13.5px;line-height:25px;color:#fff;letter-spacing:.3px;transform:translateX(-50%);white-space:nowrap}
.main-nav li.current{background:var(--wine);width:64px;height:25px;text-align:center}
.main-nav .sep{position:absolute;top:23px;width:1px;height:18px;background:#7d86b8}

.slider{left:145px;top:160px;width:908px;height:384px;border:2px solid #fff;box-shadow:0 2px 4px rgba(0,0,0,.35);overflow:hidden;z-index:2}
.slide-photo{position:absolute;inset:0;background:radial-gradient(circle at 25% 20%,#6a7a2a 0,#3d4a18 25%,transparent 45%),radial-gradient(circle at 85% 40%,#c9b9a5 0,#8d7d6a 30%,transparent 55%),linear-gradient(110deg,#5a3a20 0%,#9a6a40 35%,#d8cbb8 60%,#7a5a38 100%)}
.slide-caption{left:9px;top:119px;width:461px;height:158px;background:rgba(20,20,20,.82)}
.slide-caption .line{position:absolute;font-family:"Libre Baskerville",Georgia,serif;color:#fff;white-space:nowrap;line-height:1}
.slide-caption .welcome{left:16px;top:24px;font-size:22px}
.slide-caption .welcome b{font-weight:700;font-size:28px}
.slide-caption .tagline{left:44px;top:55px;font-size:17px}
.slide-caption .tagline span{font-family:"Alfa Slab One",Georgia,serif;color:var(--yellow);font-size:23px}
.slide-caption .stores{left:72px;top:84px;font-size:19px}
.slide-caption .stores small{font-size:14px}
.read-more{left:65px;top:116px;width:146px;height:34px;background:#000;border-radius:8px;color:#fff;font-family:"Libre Baskerville",Georgia,serif;font-size:15px;line-height:34px;text-align:center}
.slide-dots{right:26px;top:28px;display:flex;gap:9px}
.slide-dots i{width:11px;height:11px;background:#fff;display:block}
.slide-dots i.on{background:#f5c400}

.panel{background:var(--panel);border:1px solid var(--panel-border);z-index:3}
.panel-head{height:44px;background:var(--wine);color:#fff;font-weight:700;font-size:14.5px;display:flex;align-items:center;padding-left:17px;gap:10px}
.panel-head.blue{background:var(--navy)}
.star{width:26px;height:26px}

.feature .item-name{left:12px;top:64px;font-size:11.5px;font-weight:700;line-height:13px;width:100px}
.feature .thumb{left:135px;top:58px;width:96px;height:64px;border:2px solid #fff;background:linear-gradient(135deg,#4a3020,#8a5a38 50%,#3a2a1a)}
.feature .rule{left:12px;top:93px;width:94px;height:1px;background:var(--rule)}
.feature .price{left:13px;top:106px;font-size:17px;color:var(--price)}
.btn-gold{background:linear-gradient(#f8cd2c,var(--gold-dark));border:1px solid #c98a00;border-radius:4px;color:#fff;text-align:center;box-shadow:0 1px 2px rgba(0,0,0,.3)}
.feature .btn-gold{left:133px;top:132px;width:99px;height:25px;line-height:24px;font-size:14px}

.product .thumb{width:131px;height:89px;border:2px solid #6e0a0a;background:linear-gradient(135deg,#6a3a20,#a86a40 50%,#5a3218)}
.product .name{font-size:11.5px;font-weight:700}
.product .price{font-size:17px;color:var(--price);text-align:right;width:80px}
.product .copy{width:262px;font-size:9.5px;line-height:12.3px}
.product .btn-gold{width:70px;height:21px;line-height:20px;font-size:10px}
.divider{height:1px;background:var(--rule)}

.adopt{left:877px;top:575px;width:178px;height:178px;background:linear-gradient(#7bb3a5,var(--teal));z-index:3}
.adopt p{position:absolute;width:100%;text-align:center;font-family:Arimo,Arial,sans-serif;font-weight:700;color:#1d2a28}
.adopt .sign{left:24px;top:128px;width:134px;height:46px;background:#f4f4f4;color:#222;font-family:"Libre Baskerville",Georgia,serif;font-size:20px;line-height:46px;text-align:center;transform:rotate(-2deg)}

.stores-panel .addr{left:12px;top:58px;font-size:10.4px;line-height:12.3px}
.stores-panel .addr p + p{margin-top:12px}

.pets-left{left:0;top:731px;width:170px;height:258px;z-index:2;background:radial-gradient(ellipse at 45% 50%,#e4e4e4 0,#a8a8a8 45%,rgba(160,160,160,0) 70%)}
.pet-right{left:1030px;top:862px;width:100px;height:216px;z-index:2;background:radial-gradient(ellipse at 50% 50%,#d9a060 0,#b07840 45%,rgba(150,100,60,0) 70%)}

.footer{left:0;top:972px;width:1200px;height:112px;z-index:1;background:repeating-linear-gradient(135deg,var(--wine) 0 3px,var(--wine-dark) 3px 5px)}
.footer-links{left:159px;top:21px;font-size:11.5px;color:#fff;display:flex;gap:9px}
.footer-copy{left:158px;top:52px;font-size:11.5px;color:#fff}
.footer-mark{left:860px;top:46px;font-family:"Libre Baskerville",Georgia,serif;font-weight:700;font-size:32px;color:rgba(255,255,255,.22)}
</style>
</head>
<body>
<div class="abs top-strip"></div>

<div class="abs brand">Critter Glow</div>

<nav class="abs main-nav">
  <svg width="496" height="54" viewBox="0 0 496 54"><polygon points="6,8 496,3 496,50 0,54" fill="var(--navy)"/></svg>
  <ul>
    <li class="current" style="left:54px">Home</li>
    <li class="sep" style="left:117px"></li>
    <li style="left:176px">About&nbsp;&nbsp;Us</li>
    <li class="sep" style="left:249px"></li>
    <li style="left:295px">Pets</li>
    <li class="sep" style="left:354px"></li>
    <li style="left:420px">Contact&nbsp;&nbsp;Us</li>
  </ul>
</nav>

<section class="abs slider">
  <div class="slide-photo" role="img" aria-label="Photo of a puppy and a kitten sitting together in a wicker basket among yellow flowers"></div>
  <div class="abs slide-caption">
    <div class="line welcome">Welcome To <b>Critter Glow</b></div>
    <div class="line tagline">your <span>PET SUPERSTORES</span></div>
    <div class="line stores"><small>at</small> Wexley and Marrow Lake</div>
    <div class="abs read-more">Read More</div>
  </div>
  <div class="abs slide-dots"><i class="on"></i><i></i><i></i><i></i><i></i></div>
</section>

<div class="abs pets-left" role="img" aria-label="Photo group of a parrot, great dane, french bulldog, rabbit and kitten"></div>

<section class="abs panel feature" style="left:146px;top:574px;width:248px;height:179px">
  <div class="panel-head"><svg class="star" viewBox="0 0 24 24"><polygon points="12,1 15,9 23,9 16.5,14 19,22 12,17 5,22 7.5,14 1,9 9,9" fill="#f5b800"/></svg>Product of the week</div>
  <div class="abs item-name">Albino Red Tiger Oscar (Tropical</div>
  <div class="abs thumb" role="img" aria-label="Photo of an albino red tiger oscar fish"></div>
  <div class="abs rule"></div>
  <div class="abs price">$241.00</div>
  <div class="abs btn-gold">View Details</div>
</section>

<section class="abs panel feature" style="left:146px;top:768px;width:248px;height:179px">
  <div class="panel-head"><svg class="star" viewBox="0 0 24 24"><polygon points="12,1 15,9 23,9 16.5,14 19,22 12,17 5,22 7.5,14 1,9 9,9" fill="#f5b800"/></svg>Animal of the week</div>
  <div class="abs item-name">Albino Red Tiger Oscar (Tropical</div>
  <div class="abs thumb" role="img" aria-label="Photo of an albino red tiger oscar fish"></div>
  <div class="abs rule"></div>
  <div class="abs price">$241.00</div>
  <div class="abs btn-gold">View Details</div>
</section>

<section class="abs panel product" style="left:412px;top:574px;width:445px;height:373px">
  <div class="panel-head blue">Products Details</div>
  <div class="abs thumb" style="left:17px;top:65px" role="img" aria-label="Photo of a Stimson python on bark"></div>
  <div class="abs name" style="left:167px;top:66px">Stimson Python</div>
  <div class="abs price" style="left:346px;top:62px">$241.00</div>
  <div class="abs copy" style="left:167px;top:91px">Lorem ipsum dolor sit amet, consectetuer adipiscing elit, sed diam nonummy nibh euismod tincidunt ut laoreet dolore magna aliquam erat volutpat. Ut wisi enim ad minim veniam, quis nostrud exerci tation ullamcorper suscipit lobortis nisl ut aliquip ex ea commodo consequat.</div>
  <div class="abs btn-gold" style="left:353px;top:163px">View Details</div>
  <div class="abs divider" style="left:21px;top:193px;width:404px"></div>
  <div class="abs thumb" style="left:17px;top:225px" role="img" aria-label="Photo of a Stimson python on bark"></div>
  <div class="abs name" style="left:167px;top:226px">Stimson Python</div>
  <div class="abs price" style="left:346px;top:222px">$241.00</div>
  <div class="abs copy" style="left:167px;top:251px">Lorem ipsum dolor sit amet, consectetuer adipiscing elit, sed diam nonummy nibh euismod tincidunt ut laoreet dolore magna aliquam erat volutpat. Ut wisi enim ad minim veniam, quis nostrud exerci tation ullamcorper suscipit lobortis nisl ut aliquip ex ea commodo consequat.</div>
  <div class="abs btn-gold" style="left:353px;top:323px">View Details</div>
</section>

<section class="abs adopt" role="img" aria-label="Illustration of a shelter dog holding a sign, promoting pet club sign up">
  <p style="top:6px;font-size:17px">Save a life.</p>
  <p style="top:28px;font-size:17px">Adopt a shelter pet.</p>
  <div class="abs sign">Sign&nbsp;&nbsp;Up</div>
</section>

<section class="abs panel stores-panel" style="left:877px;top:768px;width:178px;height:179px">
  <div class="panel-head" style="padding-left:10px;gap:8px"><svg width="24" height="24" viewBox="0 0 24 24"><circle cx="12" cy="12" r="11" fill="#fff"/><path d="M12 5a5 5 0 0 0-5 5c0 4 5 9 5 9s5-5 5-9a5 5 0 0 0-5-5zm0 7a2 2 0 1 1 0-4 2 2 0 0 1 0 4z" fill="var(--wine)"/></svg>Store Locations</div>
  <div class="abs addr">
    <p>Shop 8 / 1500 Harbour Hwy<br>WEXLEY W.A 6190<br>Phone: (08) 5550 1970<br>Fax: (08) 5550 1960</p>
    <p>Unit 1 / 10 Horizon Drive<br>MARROW LAKE W.A 6195<br>Phone: (08) 5550 6619<br>Fax: (08) 5550 6613</p>
  </div>
</section>

<footer class="abs footer">
  <div class="abs footer-links"><span>Home</span><span>|</span><span>About Us</span><span>|</span><span>Pets |</span><span>Contact Us</span></div>
  <div class="abs footer-copy">2012-2013 - Rights have been reserved by CritterGlow</div>
  <div class="abs footer-mark">Critter Glow</div>
</footer>

<div class="abs pet-right" role="img" aria-label="Photo of a ginger tabby kitten standing"></div>
</body>
</html>
```